Generative AI radar Infographics

I want to create an infographic called "Automated Reasoning Horizon Chart for Tender Replies". (see slide 3 of the PowerPoint file). I want to use it on social media (Pellocast and Website). I added 2 inspiration graphics in my brief (see slide 2 of the PowerPoint). I want to add my logo on the infographic. (I also uploaded my company logos). You can find model detailed instructions on slide 1 of the PowerPoint.
Target Market(s)
Business development and sales
Industry/Entity Type
I am a business consultant. I will be using this infographics on Pellocast and in my powerpoint presentations to clients
Look and feel
Each slider illustrates characteristics of the customer's brand and the style your logo design should communicate.

```html
<!DOCTYPE html>
<html lang="en">
<head>
<meta charset="utf-8">
<title>Automated Reasoning Horizon Chart for Tender Replies</title>
<link rel="stylesheet" href="https://fonts.googleapis.com/css2?family=Raleway:wght@600;700&family=Lato:wght@400;700&display=swap">
<style>
  :root {
    --navy: #0b2c3f;
    --teal: #0b8fb5;
    --heading-teal: #1796be;
    --cyan-light: #c0eefc;
    --swoosh-blue: #d3ebf2;
    --swoosh-grey: #d6dadd;
    --white: #ffffff;
  }
  html, body {
    margin: 0;
    padding: 0;
    width: 1200px;
    height: 1200px;
    overflow: hidden;
    background: var(--white);
  }
  .chart-canvas {
    position: relative;
    width: 1200px;
    height: 1200px;
    font-family: "Raleway", sans-serif;
  }
  .chart-title {
    position: absolute;
    top: 92px;
    left: 0;
    width: 100%;
    margin: 0;
    text-align: center;
    font-weight: 700;
    font-size: 46px;
    line-height: 58px;
    letter-spacing: -0.3px;
  }
  .chart-title .title-main { display: block; color: var(--navy); }
  .chart-title .title-sub { display: block; color: var(--heading-teal); }
  .radar { position: absolute; top: 0; left: 0; }
  .axis-label { font-family: "Raleway", sans-serif; font-weight: 700; fill: var(--heading-teal); font-size: 29px; }
  .axis-note { font-size: 21px; }
  .band-label { font-family: "Lato", sans-serif; font-weight: 700; fill: var(--white); font-size: 21px; letter-spacing: 3px; }
  .item-small { font-family: "Lato", sans-serif; font-size: 11px; }
  .item-large { font-family: "Lato", sans-serif; font-size: 14px; }
  .on-dark { fill: var(--white); }
  .on-light { fill: var(--navy); }
  .brand-mark {
    position: absolute;
    right: 92px;
    top: 1108px;
    margin: 0;
    font-family: "Raleway", sans-serif;
    font-weight: 700;
    font-size: 26px;
    color: var(--navy);
    letter-spacing: 0.5px;
  }
</style>
</head>
<body>
<main class="chart-canvas">
  <h1 class="chart-title">
    <span class="title-main">Automated Reasoning Horizon Chart</span>
    <span class="title-sub">for Tender Replies</span>
  </h1>

  <svg class="radar" width="1200" height="1200" viewBox="0 0 1200 1200" aria-label="Horizon chart with four quadrants">
    <defs>
      <path id="arc-decision" d="M 352 675 A 248 248 0 0 1 600 427"/>
      <path id="arc-development" d="M 600 427 A 248 248 0 0 1 848 675"/>
      <path id="arc-capture" d="M 330 675 A 270 270 0 0 0 600 945"/>
      <path id="arc-strategy" d="M 600 945 A 270 270 0 0 0 870 675"/>
    </defs>

    <!-- surrounding swooshes -->
    <g class="swooshes" fill="none">
      <path d="M 251 838 A 385 385 0 0 1 895 427" stroke="var(--swoosh-blue)" stroke-width="38"/>
      <path d="M 543 350 A 330 330 0 1 1 543 1000" stroke="var(--swoosh-grey)" stroke-width="28"/>
      <path d="M 938 870 A 390 390 0 0 1 262 870" stroke="var(--swoosh-blue)" stroke-width="30"/>
    </g>

    <!-- rings -->
    <circle cx="600" cy="675" r="296" fill="var(--navy)"/>
    <circle cx="600" cy="675" r="286" fill="var(--teal)"/>
    <circle cx="600" cy="675" r="230" fill="var(--white)"/>

    <!-- quadrants -->
    <path class="quad-decision" d="M 600 675 L 382 675 A 218 218 0 0 1 600 457 Z" fill="var(--navy)"/>
    <path class="quad-development" d="M 600 675 L 600 457 A 218 218 0 0 1 818 675 Z" fill="var(--cyan-light)"/>
    <path class="quad-capture" d="M 600 675 L 600 893 A 218 218 0 0 1 382 675 Z" fill="var(--cyan-light)"/>
    <path class="quad-strategy" d="M 600 675 L 818 675 A 218 218 0 0 1 600 893 Z" fill="var(--navy)"/>

    <!-- axes with arrows -->
    <g class="axes" stroke="var(--white)" stroke-width="3">
      <line x1="600" y1="392" x2="600" y2="958"/>
      <line x1="318" y1="675" x2="882" y2="675"/>
    </g>
    <g class="arrowheads" fill="var(--white)">
      <polygon points="600,380 594,396 606,396"/>
      <polygon points="600,970 594,954 606,954"/>
      <polygon points="306,675 322,669 322,681"/>
      <polygon points="894,675 878,669 878,681"/>
    </g>

    <!-- band labels -->
    <text class="band-label"><textPath href="#arc-decision" startOffset="50%" text-anchor="middle">DECISION SUPPORT</textPath></text>
    <text class="band-label"><textPath href="#arc-development" startOffset="50%" text-anchor="middle">PROPOSAL DEVELOPMENT</textPath></text>
    <text class="band-label"><textPath href="#arc-capture" startOffset="50%" text-anchor="middle">CAPTURE STRATEGY</textPath></text>
    <text class="band-label"><textPath href="#arc-strategy" startOffset="50%" text-anchor="middle">PROPOSAL STRATEGY</textPath></text>

    <!-- decision support items -->
    <g class="item-small on-dark" text-anchor="end">
      <text x="583" y="538">BID/NO BID ANALYSIS</text>
      <text x="583" y="558">BID QUALIFICATION</text>
      <text x="583" y="578">OPPORTUNITY ASSESSMENT</text>
      <text x="583" y="598">WIN PROBABILITY MODELING</text>
      <text x="583" y="618">STRATEGIC PRICING OPTIMIZATION</text>
      <text x="583" y="639">COMPLIANCE ASSESSMENT</text>
    </g>

    <!-- proposal development items -->
    <g class="item-small on-light">
      <text x="616" y="512">COMPANY PROFILE</text>
      <text x="616" y="529.5">CV AND RESUMES</text>
      <text x="616" y="547">PAST PERFORMANCE</text>
      <text x="616" y="564.5">TECHNICAL SOLUTION</text>
      <text x="616" y="582">COMPLIANCE MATRIX</text>
      <text x="616" y="599.5">STATEMENT OF WORK</text>
      <text x="616" y="617">EXECUTIVE SUMMARY</text>
      <text x="616" y="634.5">SECURITY QUESTIONNAIRES</text>
      <text x="616" y="652">DUE DILIGENCE QUESTIONNAIRES</text>
    </g>

    <!-- capture strategy items -->
    <g class="item-small on-light" text-anchor="end">
      <text x="583" y="709">CAPTURE PLAN</text>
      <text x="583" y="731">SWOT ANALYSIS</text>
      <text x="583" y="753">CUSTOMER HOT BUTTONS</text>
      <text x="583" y="776">CUSTOMER INTELLIGENCE</text>
      <text x="583" y="798">COMPETITIVE INTELLIGENCE</text>
      <text x="583" y="820">VALUE PROPOSITION</text>
    </g>

    <!-- proposal strategy items -->
    <g class="item-large on-dark">
      <text x="616" y="708">PROPOSAL PLAN</text>
      <text x="616" y="730">PROPOSAL OUTLINE</text>
      <text x="616" y="752">DIFFERENTIATORS</text>
      <text x="616" y="774">WIN THEME</text>
      <text x="616" y="796">EXTRACTION</text>
      <text x="616" y="818">KEY MESSAGES</text>
      <text x="616" y="840">EXTRACTION</text>
    </g>

    <!-- axis labels -->
    <g class="axis-label" text-anchor="middle">
      <text x="600" y="319">Process</text>
      <text x="600" y="349">Enhancement</text>
      <text x="600" y="1025">Strategy</text>
      <text x="600" y="1054">Enablement</text>
    </g>
    <g class="axis-label" text-anchor="end">
      <text x="268" y="642">Insights</text>
      <text x="268" y="671">Generation</text>
      <text x="268" y="698" class="axis-note">(Transformative</text>
      <text x="268" y="725" class="axis-note">application)</text>
    </g>
    <g class="axis-label">
      <text x="927" y="657">Task</text>
      <text x="927" y="686">Automation</text>
      <text x="927" y="713" class="axis-note">(Foundational Use)</text>
    </g>
  </svg>

  <p class="brand-mark">Kestrel Advisory Group</p>
</main>
</body>
</html>
```